Flyer Design Project

A beauty salon Velmora Spa needs a flyer design to promote some new services that are available in the salon. These are anti-aging, slimming and other treatments performed on the modern high-tech cosmetological equipment.
The flyer will be distrubuted in hi-end supermarket located near the salon. It would go inside the bags when the purchases are packed at the cashier desk.
The main idea is make people read it and not to throw it away immediately. The flyer will be printed on the top quality paper.
There will either be a discound or a promotional treatment in the flyer.
We are not sure about the size of the flyer. It should not be too big neither too small. Ideally on the one side there should be information about Facial Treatments and on the other about the Body Treatments. However we are open for other suggestions of the Pixel Harbor.
This is our web-site www.velmora-spa.ru
Though being in Russian, it may give you an idea of our concept.
Updates

Thanks for all the designs submitted.

One general comment would be - the flyer should look different from the usual flyer one might get regarding the beauty salon services. Please make it attractive and unusual. Thanks.

Target Market(s)

Ladies from 25 to 60 years old who are well-to-do

Industry/Entity Type

Beauty Salon

Requirements
Nice to have
• It would be nice to have some technical features in the design.
Should not have
• The flyer should not be overloaded with pictures or graphic design features. It should be elegant and clear. The design should not look too "spa" as we promote technological treatments not massages.

```html
<!DOCTYPE html>
<html lang="ru">
<head>
<meta charset="utf-8">
<title>Velmora Spa — флаеры</title>
<link rel="stylesheet" href="https://fonts.googleapis.com/css2?family=PT+Sans:wght@400;700&family=Open+Sans:wght@400;600&display=swap">
<style>
  :root{
    --page:#efe7dc;
    --frame:#3a1a14;
    --band:#2d140f;
    --band-plate:#46261e;
    --paper-top:#ddd0c0;
    --paper-bottom:#c9b6a1;
    --heading:#3a1a14;
    --body:#6b4d3f;
    --rule:#5a3629;
    --logo:#ffffff;
  }
  *{box-sizing:border-box;margin:0;padding:0}
  html,body{width:1200px;height:907px;overflow:hidden;background:var(--page)}
  .canvas{position:relative;width:1200px;height:907px}
  .flyer-shadow{position:absolute;top:191px;width:556px;height:556px;filter:drop-shadow(0 6px 10px rgba(60,30,20,.35))}
  .flyer-shadow.face{left:36px}
  .flyer-shadow.body{left:613px}
  .flyer{position:absolute;inset:0;background:var(--frame);
    clip-path:polygon(50% 0,100% 50%,50% 100%,0 50%)}
  .flyer-inner{position:absolute;inset:16px;overflow:hidden;
    clip-path:polygon(50% 0,100% 50%,50% 100%,0 50%);
    background:linear-gradient(180deg,var(--paper-top),var(--paper-bottom))}
  .photo{position:absolute;left:0;right:0;top:0;height:212px}
  .face .photo{background:linear-gradient(160deg,#f7efe9 0%,#ecd2c1 45%,#c79478 75%,#6e3d26 100%)}
  .body .photo{background:linear-gradient(170deg,#f6f4f3 0%,#ece9e8 60%,#d9d5d4 100%)}
  .band{position:absolute;left:0;right:0;top:208px;height:54px;background:var(--band)}
  .logo-plate{position:absolute;left:50%;top:0;transform:translateX(-50%);width:300px;height:54px;
    background:var(--band-plate);display:flex;align-items:center;justify-content:center;gap:9px}
  .logo-dot{width:14px;height:14px;border-radius:50%;background:var(--logo)}
  .logo-name{font-family:"Open Sans",sans-serif;font-weight:400;font-size:25px;color:var(--logo);letter-spacing:.2px;line-height:1}
  .content{position:absolute;left:0;right:0;top:0;text-align:center;color:var(--body)}
  .content>*{position:absolute;left:50%;transform:translateX(-50%);white-space:nowrap}
  .section-title{font-family:"PT Sans",sans-serif;font-weight:700;font-size:14px;color:var(--heading);
    text-transform:uppercase;letter-spacing:.4px;padding-bottom:3px;border-bottom:1px solid var(--rule);width:130px}
  .service-title{font-family:"PT Sans",sans-serif;font-weight:700;font-size:10.5px;color:var(--heading);text-transform:uppercase}
  .service-text{font-family:"PT Sans",sans-serif;font-size:8px;line-height:10.5px}
  .service-text span{display:block}
  .divider{width:80px;height:1px;background:var(--rule)}
  .contacts{font-family:"PT Sans",sans-serif;font-size:5.5px;line-height:7.5px}
  .contacts span{display:block}
  .end-dot{width:4px;height:4px;border-radius:50%;background:var(--frame)}
</style>
</head>
<body>
<main class="canvas">

  <section class="flyer-shadow face">
    <div class="flyer">
      <div class="flyer-inner">
        <div class="photo" role="img" aria-label="Фотография: женщина с закрытыми глазами отдыхает на процедуре ухода за лицом, рядом свеча и брусочки мыла"></div>
        <div class="band"><div class="logo-plate"><span class="logo-dot"></span><span class="logo-name">velmora spa</span></div></div>
        <div class="content">
          <h2 class="section-title" style="top:272px">Для лица</h2>
          <h3 class="service-title" style="top:300px">Косметология</h3>
          <p class="service-text" style="top:314px">
            <span>Ваша кожа заслуживает самого лучшего! В центре философии нашего салона всегда находится</span>
            <span>клиент, его красота и благополучие. Программы для кожи лица — это изысканные</span>
            <span>spa-ритуалы, в которых решение эстетических задач неразрывно связано с благотвор-</span>
            <span>ным воздействием на все органы чувств, комфортной релаксацией и</span>
            <span>пробуждением энергии.</span>
          </p>
          <h3 class="service-title" style="top:382px">Аппаратная косметология</h3>
          <p class="service-text" style="top:396px">
            <span>Мы работаем по эксклюзивным технологиям восстановления</span>
            <span>кожи, устраняя признаки старения. Процедура</span>
            <span>лифтинга — это на 100% безопасное,</span>
            <span>безболезненное и абсолютно</span>
            <span>естественное воздействие</span>
            <span>на кожу.</span>
          </p>
        </div>
      </div>
    </div>
  </section>

  <section class="flyer-shadow body">
    <div class="flyer">
      <div class="flyer-inner">
        <div class="photo" role="img" aria-label="Фотография: специалист проводит аппаратный массаж тела клиентке на кушетке рядом с косметологическим аппаратом"></div>
        <div class="band"><div class="logo-plate"><span class="logo-dot"></span><span class="logo-name">velmora spa</span></div></div>
        <div class="content">
          <h2 class="section-title" style="top:272px">Для тела</h2>
          <h3 class="service-title" style="top:298px">VLX активация вашей красоты</h3>
          <p class="service-text" style="top:312px">
            <span>Липомассаж — запатентованная технология восстановления активности жировых клеток для уменьшения</span>
            <span>объёмов жировых отложений, восстановления тонуса кожи и моделирования контуров тела.</span>
          </p>
          <h3 class="service-title" style="top:340px">Массаж</h3>
          <p class="service-text" style="top:354px">
            <span>классический массаж • массаж спины • антицеллюлитный массаж</span>
            <span>массаж «Плоский животик» • лимфодренажный массаж</span>
          </p>
          <h3 class="service-title" style="top:382px">SPA уходы «Магия минералов»</h3>
          <p class="service-text" style="top:396px">
            <span>Программа подходит для глубокого питания кожи, нормализации</span>
            <span>обменных процессов, дренажа, повышения упругости кожи</span>
            <span>и улучшения её текстуры.</span>
          </p>
          <div class="divider" style="top:440px"></div>
          <p class="contacts" style="top:444px">
            <span>телефоны: +7 (495) 284-61-30 • +7 (926) 517-40-92</span>
          </p>
          <div class="divider" style="top:454px"></div>
          <p class="contacts" style="top:458px">
            <span>Адрес: Москва, ул. Липовая, д. 14,</span>
            <span>ТЦ «Лесной», 2 этаж</span>
            <span>E-mail: info@velmora-spa.ru</span>
          </p>
          <div class="end-dot" style="top:486px"></div>
        </div>
      </div>
    </div>
  </section>

</main>
</body>
</html>
```